Business Card for a recruitment agency specializing in engineers and geeks.

I am looking to create Business Card Design for my company.
That
## Company name:
Quorvant Inc.
Quorvant is a term coined from the following concepts.
1. geek + engineer
2. geek utopia
## Company Description:
The concept of the company is to be a recruitment agency that creates a paradise for geeky engineers. We want to be a place where engineers can have more freedom and ideal career support.
# Target.
The noun itself is often given to companies that want to hire engineers, geeks, and IT-related personnel, so it would be nice to get the impression that this company seems to have good engineers and IT personnel. There are many occasions where I meet with the human resources department, president, or senior management and give it to them.
# Atmosphere
We are happy with simplicity, but with an impact that will help people remember the company. The logo is based on a dinosaur that does programming, so it should be somewhat playful, but since it will basically be used in a business setting, please don't make it too silly.
# About the logo
See the attached files. The company logo represents our engineers smiling upward because of our work, with the motif of a dinosaur doing programming.
## Color
We will leave the color scheme to you, but since the logo is in black and white, colors with such a taste would fit well.
## file format
ai, psd, png, svg
Industry/Entity Type
human resource and employment agency
Contact Information for Business Card
Company name, address, email, tel, URL,logo
Colors
Designer to choose colors to be used in the design.

```html
<!DOCTYPE html>
<html lang="en">
<head>
<meta charset="utf-8">
<title>Quorvant Inc. — Business Card</title>
<link rel="stylesheet" href="https://fonts.googleapis.com/css2?family=Open+Sans:wght@400;700&display=swap">
<style>
  :root {
    --backdrop: #4a4c50;
    --ink: #1b1b1c;
    --paper: #ffffff;
    --muted: #d9d9d9;
  }
  * { margin: 0; padding: 0; box-sizing: border-box; }
  html, body {
    width: 1200px; height: 874px; overflow: hidden;
    background: var(--backdrop);
    font-family: "Open Sans", Arial, sans-serif;
  }
  .card {
    position: absolute;
    left: 280px;
    width: 640px; height: 366px;
    border-radius: 22px;
    overflow: hidden;
    background: var(--ink);
  }
  .card--back { top: 40px; }
  .card--front { top: 456px; }

  .brand {
    position: absolute;
    display: flex; align-items: center; gap: 16px;
    font-weight: 700;
    letter-spacing: 1px;
  }
  .brand__mark { display: block; }
  .card--back .brand {
    left: 50%; top: 50%; transform: translate(-50%, -50%);
    color: var(--paper); font-size: 48px;
  }
  .card--back .brand__mark { width: 40px; height: 40px; background: var(--paper); }

  .front-shape { position: absolute; inset: 0; }
  .card--front .brand {
    left: 56px; top: 120px;
    flex-direction: column; align-items: flex-start; gap: 14px;
    color: var(--ink); font-size: 40px;
  }
  .card--front .brand__mark { width: 52px; height: 52px; background: var(--ink); }

  .contact {
    position: absolute;
    right: 40px; top: 112px;
    text-align: right;
    color: var(--paper);
  }
  .contact__name { font-size: 22px; font-weight: 700; line-height: 1.1; }
  .contact__role { font-size: 13px; color: var(--muted); margin-bottom: 26px; }
  .contact__line {
    display: flex; justify-content: flex-end; align-items: center; gap: 10px;
    font-size: 13px; line-height: 22px;
  }
  .contact__icon { width: 12px; height: 12px; fill: var(--paper); flex: none; }
</style>
</head>
<body>
  <section class="card card--back">
    <div class="brand"><span class="brand__mark"></span><span class="brand__name">Quorvant</span></div>
  </section>

  <section class="card card--front">
    <svg class="front-shape" viewBox="0 0 640 366" aria-hidden="true">
      <path fill="#ffffff" d="M0,0 H250 C262,0 266,10 263,22 L233,150 C228,182 246,204 292,212 C252,218 232,236 227,270 L215,366 H78 L0,296 Z"/>
    </svg>
    <div class="brand"><span class="brand__mark"></span><span class="brand__name">Quorvant</span></div>
    <div class="contact">
      <div class="contact__name">Daniel Harlow</div>
      <div class="contact__role">Managing Director</div>
      <div class="contact__line">000-000-0000
        <svg class="contact__icon" viewBox="0 0 24 24"><path d="M6.6 10.8a15.1 15.1 0 0 0 6.6 6.6l2.2-2.2a1 1 0 0 1 1-.25 11.4 11.4 0 0 0 3.6.57 1 1 0 0 1 1 1V20a1 1 0 0 1-1 1A17 17 0 0 1 3 4a1 1 0 0 1 1-1h3.5a1 1 0 0 1 1 1c0 1.25.2 2.45.57 3.57a1 1 0 0 1-.25 1z"/></svg>
      </div>
      <div class="contact__line">d.harlow@quorvant.com
        <svg class="contact__icon" viewBox="0 0 24 24"><path d="M2 5h20v14H2z M2 5l10 8 10-8" fill="#fff" stroke="#1b1b1c" stroke-width="1.5"/></svg>
      </div>
      <div class="contact__line">www.quorvant.com
        <svg class="contact__icon" viewBox="0 0 24 24"><circle cx="12" cy="12" r="10" fill="none" stroke="#fff" stroke-width="2"/><path d="M2 12h20M12 2c3 3 3 17 0 20M12 2c-3 3-3 17 0 20" fill="none" stroke="#fff" stroke-width="1.6"/></svg>
      </div>
    </div>
  </section>
</body>
</html>
```